BRW Be The Man

I need a 2 sided flyer 8.5x11. I want the design to be similar and the words on the front to be the same as attached. Instead of the stadium on right side, use the pics attached.
The following Words/quotes on the back of flyer other pictures:
—Take the road less travelled and watch it make ALL the difference...

—My sons wanted to stay at BRW because they had teachers and coaches that truly cared about them in the classroom and on the field and court. Does your son want to be a big fish in a little pond or a little fish in a big pond?Doreen Malby, Parent of Everett ‘16 and Reid ‘18

—The kids and teachers at BRW lift each other up. Everyone is raised up by higher expectations and standards of performance, work ethic and behavior. Glen Ostrow, Parent Of Tobias ‘18

—Ultimately BRW prepared me for college and the challenges of being a student-athlete at the University of Carrowmere. I was better prepared to balance school and baseball compared to my fellow teammates from different high schools around the country.

Reid Hallam ‘13, PBA First Round draft pick of OT Harriers

```html
<!DOCTYPE html>
<html lang="en">
<head>
<meta charset="utf-8">
<title>BRW Be The Man – Flyer Back</title>
<link rel="stylesheet" href="https://fonts.googleapis.com/css2?family=Lato:wght@700;900&display=swap">
<style>
  :root {
    --sky-light: #d4eef9;
    --sky-mid: #8fd3f1;
    --sky-deep: #4cc3ee;
    --navy: #0e3c61;
    --navy-deep: #0b3a66;
    --ink: #133e60;
    --frame: #ffffff;
    --photo-night: #1d2a4a;
    --photo-blue: #2f5fb0;
    --photo-field: #4d6a46;
  }
  * { margin: 0; padding: 0; box-sizing: border-box; }
  html, body { width: 1200px; height: 994px; overflow: hidden; }
  body { font-family: "Lato", sans-serif; background: var(--sky-mid); }
  .flyer {
    position: relative;
    width: 1200px;
    height: 994px;
    overflow: hidden;
    background: linear-gradient(160deg, var(--sky-light) 0%, #b3e1f5 40%, var(--sky-mid) 75%, var(--sky-deep) 100%);
  }
  .flyer__backdrop { position: absolute; inset: 0; }
  .headline {
    position: absolute;
    top: 92px;
    left: 0;
    width: 100%;
    text-align: center;
    font-weight: 900;
    font-size: 63px;
    line-height: 80px;
    letter-spacing: -0.5px;
    color: var(--navy);
  }
  .testimonials {
    position: absolute;
    top: 285px;
    left: 70px;
    width: 1060px;
    text-align: center;
    color: var(--ink);
    font-weight: 700;
    font-size: 16.6px;
    line-height: 23.5px;
  }
  .testimonial + .testimonial { margin-top: 23px; }
  .photo {
    position: absolute;
    border: 4px solid var(--frame);
  }
  .photo--huddle {
    left: 51px; top: 596px; width: 326px; height: 300px;
    background: radial-gradient(circle at 40% 40%, var(--photo-blue), var(--photo-night) 80%);
  }
  .photo--entrance {
    left: 372px; top: 561px; width: 456px; height: 368px;
    z-index: 2;
    background: linear-gradient(180deg, #7f9a7a 0%, var(--photo-field) 30%, #c9d0d6 55%, #2a3340 80%, var(--photo-field) 100%);
  }
  .photo--tunnel {
    left: 823px; top: 596px; width: 326px; height: 300px;
    background: radial-gradient(circle at 50% 55%, var(--photo-blue), #1a1720 85%);
  }
</style>
</head>
<body>
<main class="flyer">
  <svg class="flyer__backdrop" width="1200" height="994" viewBox="0 0 1200 994" aria-hidden="true">
    <g fill="#ffffff" opacity="0.18">
      <polygon points="520,0 640,0 300,994 180,994"/>
      <polygon points="760,0 820,0 520,994 460,994"/>
      <polygon points="980,0 1100,0 760,994 640,994"/>
      <polygon points="1150,0 1200,0 1200,120 900,994 860,994"/>
    </g>
    <polygon points="0,381 118,596 51,596 51,896 0,994" fill="var(--navy-deep)"/>
    <polygon points="0,640 60,994 0,994" fill="#1564a8" opacity="0.7"/>
    <polygon points="1060,994 1200,850 1200,994" fill="#1a6fb8" opacity="0.8"/>
    <polygon points="0,896 260,994 0,994" fill="#2a9ad6" opacity="0.6"/>
  </svg>

  <h1 class="headline">Take the road less travelled and watch<br>it make ALL the difference...</h1>

  <section class="testimonials">
    <p class="testimonial">My sons wanted to stay at BRW because they had teachers and coaches that truly cared about them in the classroom and on the field and court. Does your son want to be a big fish in a little pond or a little fish in a big pond?Doreen Malby, Parent of Everett ‘16 and Reid ‘18</p>
    <p class="testimonial">The kids and teachers at BRW lift each other up. Everyone is raised up by higher expectations and standards of performance, work ethic and behavior. Glen Ostrow, Parent Of Tobias ‘18</p>
    <p class="testimonial">Ultimately BRW prepared me for college and the challenges of being a student-athlete at the University of Carrowmere. I was better prepared to balance school and baseball compared to my fellow teammates from different high schools around the country.</p>
  </section>

  <div class="photo photo--huddle" role="img" aria-label="Football players in blue helmets raising them together in a team huddle at night"></div>
  <div class="photo photo--entrance" role="img" aria-label="Football team running onto the field through smoke behind a blue flag"></div>
  <div class="photo photo--tunnel" role="img" aria-label="Players in blue jerseys gathered at the tunnel before a night game"></div>
</main>
</body>
</html>
```